Elegant Business Card with Logo and Picture

Please create a business card that has the Logo colors add Gold and turquoise / use the attached logo - I would like a beautiful Business Card - Please make sure it's printed on both sides / Picture can go on one side Logo other
www.velmorshine.example
614-372-0586
Lyn Odessa Ferwick
lynodessaf@quillpost.example
Life Coach
Vantrell Certified Teacher / Life Coach / Interior Designer
Transformational Retreats

Target Market(s)

Women Men General

Industry/Entity Type

Life Coaching

Contact Information for Business Card

www.velmorshine.example
614-372-0586
Lyn Odessa Ferwick
Life Coach
Vantrell Certified Teacher / Yoga Teacher / Interior Designer

Font styles to use
Serif
Decorative

Colors
33a6d6
e34197
ffc214

Requirements
Must have
• Quality Paper and touch /
Nice to have
• Beautiful Touch and feel
Should not have
• needs to be elegant

```html
<!DOCTYPE html>
<html lang="en">
<head>
<meta charset="UTF-8">
<title>Velmor Shine Coaching – Business Card</title>
<link rel="stylesheet" href="https://fonts.googleapis.com/css2?family=Zilla+Slab:wght@400;500&family=Parisienne&display=swap">
<style>
  :root {
    --stage: #2a2c31;
    --card: #0b0b0c;
    --card-edge: #1a1a1c;
    --turquoise: #3cc8c0;
    --gold: #d6a83a;
    --ink: #e9e9e9;
  }
  * { margin: 0; padding: 0; box-sizing: border-box; }
  html, body { width: 1200px; height: 900px; overflow: hidden; }
  body {
    background: var(--stage);
    font-family: "Zilla Slab", Georgia, serif;
    position: relative;
  }
  .card {
    position: absolute;
    width: 640px;
    height: 366px;
    left: 280px;
    background: var(--card);
    border: 1px solid var(--card-edge);
    border-radius: 4px;
    overflow: hidden;
    box-shadow: 0 18px 40px rgba(0,0,0,0.45);
  }
  .card--brand { top: 60px; }
  .card--contact { top: 470px; }

  /* Brand side */
  .brand-name {
    position: absolute;
    left: 0; right: 0; top: 112px;
    text-align: center;
    color: var(--turquoise);
    font-weight: 500;
    letter-spacing: 0.16em;
    text-transform: uppercase;
    line-height: 1.25;
  }
  .brand-name__main { display: block; font-size: 32px; }
  .brand-name__sub { display: block; font-size: 14px; letter-spacing: 0.6em; padding-left: 0.6em; }
  .tagline {
    position: absolute;
    left: 0; right: 0; top: 226px;
    margin: 0 auto;
    width: max-content;
    color: var(--ink);
    font-size: 20px;
    padding-bottom: 8px;
    border-bottom: 2px solid var(--ink);
  }

  /* Contact side */
  .contact-brand {
    position: absolute;
    left: 34px; top: 30px;
    color: var(--turquoise);
    font-weight: 500;
    text-transform: uppercase;
    letter-spacing: 0.16em;
    line-height: 1.2;
  }
  .contact-brand__main { display: block; font-size: 21px; }
  .contact-brand__sub { display: block; font-size: 10px; letter-spacing: 0.6em; padding-left: 60px; }
  .person {
    position: absolute;
    left: 34px; top: 100px;
    width: 340px;
  }
  .person__name {
    font-family: "Parisienne", cursive;
    color: var(--gold);
    font-size: 27px;
  }
  .person__role { color: var(--turquoise); font-size: 17px; }
  .person__titles {
    color: var(--ink);
    font-size: 16px;
    line-height: 1.3;
    margin-top: 2px;
  }
  .divider {
    position: absolute;
    left: 34px; top: 200px;
    width: 300px; height: 1px;
    background: linear-gradient(90deg, var(--gold), rgba(214,168,58,0.1));
  }
  .contact-list {
    position: absolute;
    left: 34px; top: 218px;
    list-style: none;
    color: var(--ink);
    font-size: 16px;
    line-height: 1.55;
  }
  .contact-list li { display: flex; align-items: center; gap: 10px; }
  .contact-list svg { width: 14px; height: 14px; flex: none; }
  .portrait {
    position: absolute;
    right: 0; bottom: 0;
    width: 270px; height: 270px;
    background: linear-gradient(180deg, rgba(11,11,12,0) 0%, #b89a5e 25%, #c7808a 60%, #b44a6c 100%);
    opacity: 0.85;
  }
</style>
</head>
<body>

  <section class="card card--brand" aria-label="Card front">
    <p class="brand-name">
      <span class="brand-name__main">Velmor Shine</span>
      <span class="brand-name__sub">Coaching</span>
    </p>
    <p class="tagline">Transformational Retreats</p>
  </section>

  <section class="card card--contact" aria-label="Card back">
    <p class="contact-brand">
      <span class="contact-brand__main">Velmor Shine</span>
      <span class="contact-brand__sub">Coaching</span>
    </p>
    <div class="person">
      <p><span class="person__name">Lyn Odessa Ferwick</span> <span class="person__role">| Life Coach</span></p>
      <p class="person__titles">Vantrell Certified Teacher | Yoga Teacher<br>Interior Designer</p>
    </div>
    <div class="divider"></div>
    <ul class="contact-list">
      <li>
        <svg viewBox="0 0 16 16" aria-hidden="true"><circle cx="8" cy="8" r="7" fill="none" stroke="#3cc8c0" stroke-width="1.4"/><path d="M5.5 4.5l1.5 0 .6 2-1 .8a5 5 0 0 0 2.1 2.1l.8-1 2 .6v1.5c-3.5.4-6.4-2.5-6-6z" fill="#3cc8c0"/></svg>
        614-372-0586
      </li>
      <li>
        <svg viewBox="0 0 16 16" aria-hidden="true"><rect x="1.5" y="3.5" width="13" height="9" fill="none" stroke="#3cc8c0" stroke-width="1.4"/><path d="M1.5 3.5l6.5 5 6.5-5" fill="none" stroke="#3cc8c0" stroke-width="1.4"/></svg>
        lynodessaf@quillpost.example
      </li>
      <li>
        <svg viewBox="0 0 16 16" aria-hidden="true"><circle cx="8" cy="8" r="6.5" fill="none" stroke="#3cc8c0" stroke-width="1.4"/><ellipse cx="8" cy="8" rx="2.8" ry="6.5" fill="none" stroke="#3cc8c0" stroke-width="1.2"/><path d="M1.5 8h13" stroke="#3cc8c0" stroke-width="1.2"/></svg>
        www.velmorshine.example
      </li>
    </ul>
    <div class="portrait" role="img" aria-label="Portrait photo of the coach in a patterned pink top"></div>
  </section>

</body>
</html>
```